依頼詳細
参考までにヨーロッパでのウォーカーのサイトです。
https://www.brantwick.com/our-products/exercisers/the-brantwick-meadow/
https://www.felstoke.co.uk/product-page/horsewalker/

残念ながらあまり多くの写真素材が無いので、うまくイラストや説明でフォローできると幸いです。
添付の写真はこちらが利用して良い素材になります。
記載項目
社名 株式会社ジーキューエムジャパン
連絡先 03-4821-9037
メール tomura@gqm-japan.com

代理店用のスペース
サイズ
A4
ページ数
両面
希望イメージ
シンプル 複雑
単色 カラフル
暗い 明るい
日常 高級
遊び心 厳粛
未来的 伝統的
女性的 男性的
希望する色
緑系、青系
納品ファイル
• イラストレーター形式 (.ai)
• フォトショップ形式 (.psd)
補足説明
写真がうまく掲載されていなかったので追記です
■ 選んだ理由

今回は素敵な提案をありがとうございます。
少ない商材の中わかりやすいイラストなど営業担当のものも喜んでいました。

■ 提案者全員のお礼・コメント

今回はたくさんの提案ありがとうございます。
一つに選考するのに落選の皆様に心苦しい限りです。
また、別な機会に個別にお願いすることもあるかと思いますので今後ともよろしくお願いいたします

```html
<!DOCTYPE html>
<html lang="ja">
<head>
<meta charset="utf-8">
<title>LINE UP 馬用ウォーキングマシン</title>
<link rel="stylesheet" href="https://fonts.googleapis.com/css2?family=Noto+Serif+JP:wght@400;600;700&family=Noto+Sans+JP:wght@400;500&family=Oswald:wght@400&family=Barlow+Condensed:wght@400&display=swap">
<style>
:root{
  --green-dark:#1d5e1f;
  --green:#2f7d2a;
  --green-light:#5aa53a;
  --ink:#3a3a3a;
  --ink-soft:#555;
  --line:#3d8a35;
  --paper:#ffffff;
}
*{margin:0;padding:0;box-sizing:border-box}
html,body{width:848px;height:1200px;overflow:hidden;background:var(--paper)}
.sheet{position:relative;width:848px;height:1200px;font-family:"Noto Sans JP",sans-serif;color:var(--ink)}
.abs{position:absolute}
.hero{left:0;top:0;width:848px;height:161px;background:linear-gradient(90deg,#8e7a5c 0%,#c4b394 30%,#d9cdb4 55%,#b49a78 80%,#9c8162 100%)}
.hero-kicker{left:0;width:848px;top:62px;text-align:center;font-family:"Barlow Condensed",sans-serif;font-size:14px;letter-spacing:.5px;color:#fff}
.hero-title{left:0;width:848px;top:78px;text-align:center;font-family:"Noto Serif JP",serif;font-size:52px;line-height:1;color:#fff;letter-spacing:1px}
.lead{left:0;width:848px;top:180px;text-align:center;font-family:"Noto Serif JP",serif;font-weight:600;font-size:27px;color:#4a4a4a}
.intro{left:0;width:848px;top:226px;text-align:center;font-family:"Noto Serif JP",serif;font-size:12.5px;line-height:19.5px;color:var(--ink)}
.intro-note{left:0;width:848px;top:274px;text-align:center;font-size:7px;color:var(--ink-soft)}
.band{left:61px;width:726px;height:47px;background:linear-gradient(90deg,var(--green-dark) 0%,var(--green) 60%,var(--green-light) 100%);color:#fff;display:flex;align-items:center;padding-left:20px}
.band-title{font-family:"Noto Serif JP",serif;font-size:28px;letter-spacing:1px;margin-right:20px}
.band-sub{font-family:"Noto Serif JP",serif;font-size:11px;padding-top:6px}
.desc{left:81px;font-size:12px;line-height:17px;color:var(--ink)}
.specs{left:81px;font-size:11px;line-height:17px;color:var(--ink-soft);list-style:none}
.specs li{display:flex}
.specs .k{width:94px;white-space:nowrap}
.specs .k::before{content:"";display:inline-block;width:8px;height:8px;border:1px solid #777;margin-right:4px;vertical-align:-1px}
.option{left:81px;font-family:"Oswald",sans-serif;font-size:19px;line-height:1;color:var(--green)}
.opt-table{left:81px;width:215px;border-collapse:collapse;font-size:10px;color:var(--ink-soft)}
.opt-table th{background:var(--green);color:#fff;font-weight:400;height:17px;border:1px solid var(--line)}
.opt-table td{height:20.3px;border:1px solid var(--line);padding-left:8px}
.opt-table td:nth-child(2){padding-left:10px}
.photo{background:linear-gradient(180deg,#d6dde0 0%,#aab0a8 55%,#8a9a6a 100%)}
.photo.dark{background:linear-gradient(180deg,#3b3f42 0%,#26292b 60%,#4a4d4f 100%)}
.photo.roof{background:linear-gradient(180deg,#c9d3d8 0%,#8e9aa2 40%,#a5652f 70%,#6b5a3c 100%)}
.photo.gate{background:linear-gradient(180deg,#c5ccd0 0%,#9ea6a8 60%,#b89a78 100%)}
.photo.post{background:linear-gradient(180deg,#e0e2dc 0%,#6a6e6a 50%,#b4a48a 100%)}
.notes{font-size:7.5px;line-height:14px;color:var(--ink-soft)}
.cta{left:113px;top:1039px;font-family:"Noto Serif JP",serif;font-weight:600;font-size:20px;color:var(--green);letter-spacing:1px}
.company{left:273px;top:1080px;font-family:"Noto Serif JP",serif;font-size:13.5px;color:var(--ink)}
.phone{left:273px;top:1106px;display:flex;align-items:center;font-family:"Noto Serif JP",serif;font-weight:600;font-size:29px;color:var(--green);line-height:1}
.phone svg{margin-right:4px}
.mail{left:273px;top:1150px;font-family:"Noto Serif JP",serif;font-size:14.5px;color:var(--ink-soft)}
.brand{left:40px;top:1112px;display:flex;align-items:center;font-family:"Noto Serif JP",serif;font-size:27px;color:#666;letter-spacing:3px}
.brand-dot{width:40px;height:40px;border-radius:50%;background:#9a9a9a;margin-right:14px}
.agent-box{left:512px;top:1025px;width:304px;height:143px;border:1px solid #555}
</style>
</head>
<body>
<div class="sheet">

  <div class="abs hero" role="img" aria-label="馬と女性が寄り添う写真"></div>
  <div class="abs hero-kicker">HORSEWARKING MACHINE</div>
  <div class="abs hero-title">LINE UP</div>

  <h1 class="abs lead">皆様が安心してお使いになれる製品をお届けします</h1>
  <p class="abs intro">大きくわけて二つのバリエーションがあり、屋根なしの導入のしやすいタイプ。屋根付きの建築が必要なタイプの２種類です。<br>そのなかで直径が１６ｍおよび１８ｍタイプ、同時に４頭、６頭、８頭の運動ができるタイプのものになります。</p>
  <p class="abs intro-note">※価格は送料抜、税抜きの表示です。※設置費用も別になります。</p>

  <!-- Pattern A -->
  <div class="abs band" style="top:307px"><span class="band-title">PATTERN A</span><span class="band-sub">馬用ウォーキングマシン　パターンA</span></div>
  <p class="abs desc" style="top:365px">設置が容易:ウォーカー本体の基礎のみ。周囲のフェンスは直置き、もしくは地面への杭打のみ。<br>強風でも煽られにくい。低コストでの導入が可能</p>
  <ul class="abs specs" style="top:410px">
    <li><span class="k">標準価格</span><span>120万</span></li>
    <li><span class="k">屋根</span><span>なし</span></li>
    <li><span class="k">素材</span><span>メッシュタイプ</span></li>
    <li><span class="k">直径タイプ</span><span>16m／18m</span></li>
    <li><span class="k">頭数</span><span>4頭／6頭</span></li>
  </ul>
  <div class="abs option" style="top:508px">OPTION</div>
  <table class="abs opt-table" style="top:527px">
    <tr><th>サイズ</th><th>頭数</th><th>価格</th></tr>
    <tr><td>直径16m</td><td>4頭</td><td>標準価格</td></tr>
    <tr><td>直径16m</td><td>6頭</td><td>プラス25万円</td></tr>
    <tr><td>直径18m</td><td>4頭</td><td>プラス25万円</td></tr>
    <tr><td>直径18m</td><td>6頭</td><td>プラス50万円</td></tr>
  </table>
  <div class="abs photo" style="left:314px;top:438px;width:233px;height:156px" role="img" aria-label="屋根なしメッシュフェンスの円形ウォーキングマシン全景"></div>
  <div class="abs photo dark" style="left:555px;top:414px;width:234px;height:180px" role="img" aria-label="メッシュフェンスと走路の近景"></div>
  <p class="abs notes" style="left:322px;top:604px">※価格は日本の港までの価格になります。※設置場所までの送料は別途見積もりになります。<br>※設置はお客様の手配になります。※ウォーカー部はパターンBと同様のものです。</p>

  <!-- Pattern B -->
  <div class="abs band" style="top:653px"><span class="band-title">PATTERN B</span><span class="band-sub">馬用ウォーキングマシン　パターンB</span></div>
  <p class="abs desc" style="top:713px">［メリット］雨天時でも運動が可能。／［デメリット］初期導入コスト。建築期間。強風時の強度<br>馬仕切部：ご希望のカスタマイズが可能です</p>
  <ul class="abs specs" style="top:778px">
    <li><span class="k">標準価格</span><span>000万</span></li>
    <li><span class="k">屋根</span><span>あり。建築タイプ</span></li>
    <li><span class="k">素材</span><span>メッシュタイプ</span></li>
    <li><span class="k">直径タイプ</span><span>16m 4頭 もしくは6頭<br>18m 6頭 もしくは8頭</span></li>
  </ul>
  <div class="abs option" style="top:881px">OPTION</div>
  <table class="abs opt-table" style="top:900px">
    <tr><th>サイズ</th><th>頭数</th><th>価格</th></tr>
    <tr><td>直径16m</td><td>4頭</td><td>プラス280万円</td></tr>
    <tr><td>直径16m</td><td>6頭</td><td>プラス305万円</td></tr>
    <tr><td>直径18m</td><td>8頭</td><td>プラス350万円</td></tr>
  </table>
  <div class="abs photo roof" style="left:314px;top:759px;width:472px;height:144px" role="img" aria-label="屋根付き木製パネルの円形ウォーキングマシン"></div>
  <div class="abs photo gate" style="left:314px;top:912px;width:116px;height:65px" role="img" aria-label="金属製の仕切りゲート"></div>
  <div class="abs photo post" style="left:438px;top:912px;width:117px;height:65px" role="img" aria-label="仕切り部の縦格子"></div>
  <p class="abs notes" style="left:570px;top:921px">※価格は日本の港までの価格になります。<br>※設置場所までの送料は別途見積もりになります。<br>※設置はお客様の手配になります。<br>※ウォーカー部はパターンAと同様のものです。</p>

  <!-- Contact -->
  <p class="abs cta">まずはお気軽にお問い合わせください</p>
  <div class="abs brand"><span class="brand-dot"></span>G.Q.M</div>
  <p class="abs company">株式会社ジーキューエムジャパン</p>
  <p class="abs phone"><svg width="20" height="24" viewBox="0 0 20 24" aria-hidden="true"><path d="M5 2c1.5-1 3 0 3.5 1.5l1 3c.3 1-.3 2-1.2 2.4l-1.3.6c.6 3 2.4 5.8 4.8 7.6l1.2-.9c.8-.6 2-.5 2.6.3l2 2.4c1 1.2.6 2.6-.6 3.4-1.4 1-3.4 1.2-5 .4C6 19.300 2.300 13.600 2.200 7.300 2.200 5 3.400 3 5 2z" fill="currentColor"/></svg>03-4821-9037</p>
  <p class="abs mail">Mail : tomura@gqm-japan.com</p>
  <div class="abs agent-box" aria-label="代理店用スペース"></div>

</div>
</body>
</html>
```